Brochure Design Project for Home Watch company

We are a new start up company in fast growing home watch industry. We provide services in Hawaii so the design needs to be reflect that. Our web site can give you overview of what we do - www.palmcrestkeeper.com. We will service clients that own second homes in Hawaii. These properties are not necessarily income producing properties for our clients. I'm looking for 2 or 4 page brochure which will be used to market our services to potential new clients. It needs to be high quality, modern with slight Hawaiian feel (we are based on Oahu). I'm not looking for a trifold type of brochure.

We are open to various colors based on what the designer might suggest but as you can see on our home page - the main picture of the home on our site has lots of red and white which we like as well as the "head" or dot above the "i" in our logo is red. I was not able to upload the file of the main house (purchased on snapvaultpix) on here therefore I'll have to provide the original photo to the selected designer at the later time. For now I just uploaded the not purchased copy.

If you have other questions please do let me know. And lastly, I will be looking to create a business card and post card as well.

```html
<!DOCTYPE html>
<html lang="en">
<head>
<meta charset="utf-8">
<title>Palm Crest Keeper – Brochure Spread</title>
<link href="https://fonts.googleapis.com/css2?family=Montserrat:wght@400;500;600;700&family=Merienda:wght@700&family=Roboto+Slab:wght@300;700&display=swap" rel="stylesheet">
<style>
  :root{
    --bg:#3a3a3c;
    --ink:#111113;
    --paper:#ffffff;
    --red:#d62b35;
    --slate:#3d3d40;
    --muted:#cfd2d6;
    --sky:#6fa6d6;
    --sea:#2d5f8a;
  }
  *{box-sizing:border-box;margin:0;padding:0}
  html,body{width:1200px;height:789px;overflow:hidden;background:var(--bg)}
  .spread{position:absolute;left:80px;top:26px;width:1040px;height:736px;display:flex;box-shadow:0 10px 30px rgba(0,0,0,.5)}
  .page{position:relative;width:520px;height:736px;overflow:hidden}
  .back{background:linear-gradient(180deg,#0b0b0d 0%,#141416 55%,#1d2320 80%,#111 100%);color:#fff;font-family:"Montserrat",sans-serif}
  .front{background:var(--paper);font-family:"Montserrat",sans-serif}

  .contact-head{position:absolute;left:40px;top:110px;width:300px;font-weight:600;letter-spacing:.04em;text-transform:uppercase}
  .contact-head .lead{font-size:17px;line-height:1.3}
  .contact-head .lead em{font-style:normal;color:var(--red)}
  .contact-head .sub{font-size:13px;margin-top:6px}

  .contact-list{position:absolute;left:30px;top:240px;width:260px;text-align:center;list-style:none}
  .contact-list li{margin-bottom:22px}
  .contact-list svg{display:block;margin:0 auto 6px;width:16px;height:16px}
  .contact-list .label{font-size:13px;font-weight:500}
  .contact-list .phone{font-size:18px;font-weight:700}

  .photo-back{position:absolute;left:320px;top:200px;width:200px;height:330px;border:8px solid var(--paper);border-right:0;background:linear-gradient(160deg,#8fb9df 0%,#7a6a5a 45%,#5a6065 70%,#2f4b63 100%)}
  .device{position:absolute;left:50px;top:600px;width:200px;height:110px;border-radius:6px;background:linear-gradient(135deg,#2a2a2c,#6b7378 60%,#d7dade)}
  .badge{position:absolute;left:320px;top:620px;width:170px;height:64px;background:#f2f2f2;border-radius:4px}

  .brand{position:absolute;left:40px;top:48px;display:flex;align-items:center;gap:10px}
  .brand-dot{width:14px;height:14px;border-radius:50%;background:var(--red)}
  .brand-name{font-family:"Roboto Slab",serif;font-weight:700;font-size:24px;color:var(--ink)}
  .tagline{position:absolute;left:64px;top:84px;font-family:"Roboto Slab",serif;font-weight:300;font-size:13px;color:var(--ink)}

  .band-top{position:absolute;left:270px;top:92px;width:250px;height:42px;background:var(--slate)}
  .rule-top{position:absolute;left:40px;top:138px;width:480px;height:5px;background:var(--red)}
  .photo-front{position:absolute;left:0;top:150px;width:520px;height:340px;background:linear-gradient(170deg,#9cc4e6 0%,#6fa6d6 25%,#8a6d58 45%,#e8e8e6 60%,#3f7aa6 78%,#1f4666 100%)}
  .rule-bottom{position:absolute;left:0;top:496px;width:520px;height:5px;background:var(--red)}
  .promise{position:absolute;left:150px;top:512px;width:370px;height:100px;background:var(--slate);color:#fff;font-family:"Merienda",cursive;font-size:21px;line-height:1.35;padding:22px 20px 0 24px}
  .site{position:absolute;left:200px;top:650px;display:flex;align-items:center;gap:8px;font-size:13px;font-weight:500;color:var(--ink)}
  .site svg{width:13px;height:13px}
</style>
</head>
<body>
<div class="spread">
  <section class="page back">
    <div class="contact-head">
      <p class="lead">Contact us for <em>free consultation.</em></p>
      <p class="sub">You have questions? We have answers!</p>
    </div>
    <ul class="contact-list">
      <li>
        <svg viewBox="0 0 16 16"><path d="M8 1a5 5 0 0 0-5 5c0 4 5 9 5 9s5-5 5-9a5 5 0 0 0-5-5z" fill="#d62b35"/><circle cx="8" cy="6" r="2" fill="#111"/></svg>
        <span class="label">Palm Crest Keeper LLC</span>
      </li>
      <li>
        <svg viewBox="0 0 16 16"><path d="M3 6c0-2 2-3 5-3s5 1 5 3v1h-3V6H6v1H3z M4 8h8l1 6H3z" fill="#d62b35"/></svg>
        <span class="phone">808-555-0142</span>
      </li>
      <li>
        <svg viewBox="0 0 16 16"><rect x="1" y="3" width="14" height="10" fill="#d62b35"/><path d="M1 3l7 6 7-6" stroke="#111" stroke-width="1.2" fill="none"/></svg>
        <span class="label">palmcrestkeeper@mail.com</span>
      </li>
      <li>
        <svg viewBox="0 0 16 16"><rect x="1.5" y="3" width="13" height="11" fill="none" stroke="#d62b35" stroke-width="1.6"/><path d="M1.5 6h13M5 1v3M11 1v3" stroke="#d62b35" stroke-width="1.6"/></svg>
        <span class="label">Monday-Friday,<br>8am-5pm (PST).</span>
      </li>
      <li>
        <svg viewBox="0 0 16 16"><circle cx="8" cy="8" r="6.5" fill="none" stroke="#d62b35" stroke-width="1.5"/><path d="M1.5 8h13M8 1.5c-3 3-3 10 0 13M8 1.5c3 3 3 10 0 13" stroke="#d62b35" stroke-width="1.2" fill="none"/></svg>
        <span class="label">www.palmcrestkeeper.com</span>
      </li>
    </ul>
    <div class="photo-back" role="img" aria-label="Photo of a tropical villa with a pavilion and water feature, continuing from the cover"></div>
    <div class="device" role="img" aria-label="Laptop showing a house photo with a checklist"></div>
    <div class="badge" role="img" aria-label="Accredited member badge"></div>
  </section>

  <section class="page front">
    <div class="brand"><span class="brand-dot"></span><span class="brand-name">Palm Crest Keeper</span></div>
    <p class="tagline">Your Home Watch Company</p>
    <div class="band-top"></div>
    <div class="rule-top"></div>
    <div class="photo-front" role="img" aria-label="Photo of a Hawaiian villa with an infinity pool overlooking the ocean and palm trees"></div>
    <div class="rule-bottom"></div>
    <p class="promise">Providing Premiere Home<br>Watch and Concierge Services</p>
    <p class="site">
      <svg viewBox="0 0 16 16"><circle cx="8" cy="8" r="6.5" fill="none" stroke="#d62b35" stroke-width="1.5"/><path d="M1.5 8h13M8 1.5c-3 3-3 10 0 13M8 1.5c3 3 3 10 0 13" stroke="#d62b35" stroke-width="1.2" fill="none"/></svg>
      www.palmcrestkeeper.com
    </p>
  </section>
</div>
</body>
</html>
```